依頼詳細
現在、iDeCo、nISAセミナー・住宅ローンセミナーを両面や片面ずつの配布しています。今回よりQRコードで毎月のイベントから選べる方式に変更したいなと思います。その分、各セミナーの特徴を簡潔にしたいのと現在同業者との差別化になっている高い専門知識をもつFPが講師・参加費あり・相談料があり無理な勧誘が一切なしという当店舗の特徴を活かしたチラシにしたいです。
また県内ではほぼ100%(把握する限り)のこの類のセミナーはケーキ付無料セミナーなど集客に特化したものが多いです。
今回は差別化を意識したものを望みます。
記載項目
現在にチラシテンプレートをいくつか掲載します
サイズ
A6
ページ数
片面
希望イメージ
シンプル 複雑
単色 カラフル
暗い 明るい
日常 高級
遊び心 厳粛
未来的 伝統的
女性的 男性的
希望する色
緑系、青系、水色系
納品ファイル
• イラストレーター形式 (.ai)
補足説明
現在使用しているチラシデータと各セミナーのソラミネ用のURLを添付します。
①ローンセミナー
https://soramine.jp/landing_pages/view/qtr2m?_gl=1*k4p7zx*_gcl_au*QWx3NTk2MjE4OC4xNjk4ODg3NzIx&_ga=2.52914837.417208361.1701234567-398271640.1655512903

②iDeCoNISAセミナー
https://soramine.jp/landing_pages/view/58hwf?_gl=1*3r6t02b*_gcl_au*QWx3NTk2MjE4OC4xNjk4ODg3NzIx&_ga=2.64927318.417208361.1701234567-398271640.1655512903

当店の案内もURLより参考にしていただき、イメージをもって作成いただけると幸いです。
https://xwrtb.hp.soramine.jp/?_gl=1*720kq4n*_gcl_au*QWx3NTk2MjE4OC4xNjk4ODg3NzIx&_ga=2.158302746.417208361.1701234567-398271640.1655512903
よろしくお願いいたします。
2024年1月8日追記になります。
イメージとしては当店の仕組みや紹介をメイン。(認知・周知UP)
真ん中やみやすい位置に人気セミナーみたいな形でQRコードか何かで誘導してその先にLPがある形で考えています!またこの形にこだわりがあるわけではないので別案あればお願いします。最近周辺で同じ類のイベントが多いので差別化を考えています
1月14日
当店舗は毎月15万部ほどチラシをポスティングしています。
チラシのどこかに〇月イベントやセミナーといったような何月分のチラシなのか記載をしていただくとありがたいです。途中での依頼ですみませんがよろしくお願いします。
有料という部分が他とは大きく違います。ここがお客様にとっての1つのハードルになるのですが、有料する意味は色々あります。
他のFPオフィスとの差別化、支払ってでも相談したいという本気度など。
”有料だから勧誘一切なし”ということではなく、インパクトのあるワードでこの有料を表現していただけると嬉しいです。

色の配色やこちらにイメージに近いので選定させていただきました。

この度はご応募ありがとうございました。
どれも良く迷いました。
また今後ともよろしくお願いします

```html
<!DOCTYPE html>
<html lang="ja">
<head>
<meta charset="utf-8">
<title>くらしとみらいの相談室 1月セミナー</title>
<link href="https://fonts.googleapis.com/css2?family=Noto+Sans+JP:wght@400;500;700;900&family=Shippori+Mincho:wght@500;700&display=swap" rel="stylesheet">
<style>
:root{
  --green:#2f9a5b;
  --green-dark:#1f6e41;
  --green-pale:#e8f4ec;
  --ink:#2a2a2a;
  --night:#262626;
  --paper:#ffffff;
  --accent:#e0483a;
  --muted:#6b6b6b;
}
*{margin:0;padding:0;box-sizing:border-box}
html,body{width:851px;height:1200px;overflow:hidden;background:var(--paper)}
body{font-family:"Noto Sans JP",sans-serif;color:var(--ink)}
.flyer{position:relative;width:851px;height:1200px;overflow:hidden;background:var(--paper)}

.brand{position:absolute;left:0;top:0;height:100px;width:851px;background:var(--paper);z-index:3}
.brand-tab{position:absolute;left:0;top:18px;height:66px;padding:0 28px 0 22px;background:var(--green-pale);border-radius:0 40px 40px 0;display:flex;align-items:center;gap:14px}
.brand-mark{width:36px;height:36px;background:var(--green);border-radius:50%}
.brand-name{font-size:30px;font-weight:700;color:var(--green-dark);letter-spacing:.04em;white-space:nowrap}

.hero{position:absolute;left:0;top:100px;width:851px;height:700px;background:var(--night)}
.hero-photo{position:absolute;left:330px;top:0;width:521px;height:700px;background:linear-gradient(100deg,#3a3633 0%,#8c7f73 22%,#d9d1c7 48%,#ece7e1 75%,#d8d0c6 100%)}
.event-date{position:absolute;left:40px;top:130px;color:#fff;font-weight:900;font-size:62px;line-height:1;white-space:nowrap}
.event-date small{font-size:36px}
.event-info{position:absolute;left:40px;top:222px;width:290px;color:#fff;font-size:15px;line-height:1.45;white-space:nowrap}
.event-info dt{float:left;width:50px;clear:left}
.event-info dd{margin-left:50px}
.event-note{position:absolute;left:40px;top:478px;color:#dcdcdc;font-size:11px;line-height:1.5;white-space:nowrap}

.catch{position:absolute;writing-mode:vertical-rl;font-family:"Shippori Mincho",serif;font-weight:700;color:var(--ink);line-height:1;white-space:nowrap}
.catch-main{left:575px;top:160px;font-size:40px;letter-spacing:.1em}
.catch-sub{left:640px;top:300px;font-size:36px;letter-spacing:.08em}
.catch-sub em{font-style:normal;font-size:52px}

.statement{position:absolute;left:100px;top:525px;width:345px;padding:20px 24px;background:rgba(255,255,255,.94);font-size:14px;line-height:1.8;color:var(--ink);white-space:nowrap}

.seminar{position:absolute;left:34px;width:380px}
.seminar-ideco{top:815px}
.seminar-loan{top:1000px}
.seminar-tag{font-size:17px;font-weight:700;color:var(--accent);line-height:1.5}
.seminar-title{margin-top:2px;background:var(--green);color:#fff;font-size:24px;font-weight:900;padding:4px 16px;width:320px;white-space:nowrap}
.seminar-loan .seminar-title{background:none;color:var(--green-dark);padding:0;font-size:28px}
.seminar-points{list-style:none;margin-top:8px;font-size:15px;line-height:1.85;white-space:nowrap}
.seminar-points li::before{content:"";display:inline-block;width:12px;height:12px;border:2px solid var(--green);border-radius:50%;margin-right:8px;vertical-align:-1px}
.apply{position:absolute;right:0;bottom:0;font-size:12px;color:var(--muted)}

.panel{position:absolute;left:430px;width:390px;border:2px solid var(--green);background:#fff}
.panel-head{position:absolute;left:-2px;top:-20px;background:var(--green);color:#fff;font-size:18px;font-weight:700;padding:4px 26px}
.lecturers{top:860px;height:200px;display:flex;justify-content:flex-end;gap:22px;padding:28px 20px 0}
.lecturer{text-align:center;width:130px}
.lecturer-photo{width:96px;height:92px;margin:0 auto;background:linear-gradient(160deg,#c9d4dc,#8c9aa6)}
.lecturer-role{font-size:9px;color:var(--muted);margin-top:6px;line-height:1.3;white-space:nowrap}
.lecturer-name{font-size:17px;font-weight:700;margin-top:2px;white-space:nowrap}
.contact{top:1088px;height:102px;padding:22px 20px 0}
.contact-text{font-size:11.5px;line-height:1.6;color:var(--ink);white-space:nowrap}
.contact-link{position:absolute;right:20px;bottom:10px;font-size:12px;color:var(--muted)}
</style>
</head>
<body>
<main class="flyer">
  <header class="brand">
    <div class="brand-tab">
      <span class="brand-mark"></span>
      <span class="brand-name">くらしとみらいの相談室</span>
    </div>
  </header>

  <section class="hero">
    <div class="hero-photo" role="img" aria-label="窓辺で微笑む女性のポートレート写真"></div>

    <p class="event-date">1月15日<small>(月)</small></p>
    <dl class="event-info">
      <dt>時間：</dt><dd>午前 10:00-12:30<br>午後 15:00-17:30</dd>
      <dt>場所：</dt><dd>くらしとみらいの相談室みどり店<br>〒870-0000<br>大分県大分市みどり町1丁目2-3<br>ソラビル101</dd>
      <dt>費用：</dt><dd>2,000円</dd>
      <dt>申込：</dt><dd>090-1234-5678</dd>
    </dl>
    <p class="event-note">※各回定員になり次第、受付を終了します。<br>※ご予約はお電話またはWebから承ります。</p>

    <p class="catch catch-main">人生が楽しみになる</p>
    <p class="catch catch-sub"><em>〝投資〟</em>をココから</p>

    <p class="statement">当セミナーは、有料です。<br>私たちは、あなたの人生のご相談を<br>“全て”請負たくはありません。<br>本気のご相談、お待ちしております。</p>
  </section>

  <section class="seminar seminar-ideco">
    <p class="seminar-tag">初心者大歓迎</p>
    <h2 class="seminar-title">iDeCo&amp;NISA セミナー</h2>
    <ul class="seminar-points">
      <li>iDeCoとNISAの違いとは？</li>
      <li>iDeCo活用例／不向き</li>
      <li>3つのメリット／デメリット</li>
    </ul>
    <span class="apply">お申し込み</span>
  </section>

  <section class="seminar seminar-loan">
    <p class="seminar-tag">大人気</p>
    <h2 class="seminar-title">住宅ローンセミナー</h2>
    <ul class="seminar-points">
      <li>頭金を入れてはいけない理由とは？</li>
      <li>繰り上げ返済をしてはいけない理由とは？</li>
      <li>借入期間を最長にするべき理由とは？</li>
    </ul>
    <span class="apply">お申し込み</span>
  </section>

  <section class="panel lecturers">
    <h3 class="panel-head">講師</h3>
    <div class="lecturer">
      <div class="lecturer-photo" role="img" aria-label="講師 高野 誠一郎の写真"></div>
      <p class="lecturer-role">住宅ローンアドバイザー<br>FP1級技能士</p>
      <p class="lecturer-name">高野 誠一郎</p>
    </div>
    <div class="lecturer">
      <div class="lecturer-photo" role="img" aria-label="講師 森田 健太の写真"></div>
      <p class="lecturer-role">住宅ローンアドバイザー<br>AFP 認定者</p>
      <p class="lecturer-name">森田 健太</p>
    </div>
  </section>

  <section class="panel contact">
    <h3 class="panel-head">お問い合わせ</h3>
    <p class="contact-text">〒870-0000 大分県大分市みどり町1丁目2-3 ソラビル101<br>くらしとみらいの相談室みどり店<br>TEL 090-1234-5678</p>
    <span class="contact-link">詳細はこちら</span>
  </section>
</main>
</body>
</html>
```